Brightpath Home Partners, LLC

We are private duty home care agency. We provide in-home care for people of all ages. Our kind natured and patient caregivers provide assistance to those who have difficulty with caring for themselves. We already have a logo designed by ArtMarketly

```html
<!DOCTYPE html>
<html lang="en">
<head>
<meta charset="utf-8">
<title>Brightpath Home Partners, LLC</title>
<link href="https://fonts.googleapis.com/css2?family=Roboto:wght@400;500;700&display=swap" rel="stylesheet">
<style>
  :root {
    --lime: #b0f50a;
    --orange: #f5520c;
    --brand-green: #3f9e1c;
    --sky: #dcedf3;
    --ink: #111111;
    --white: #ffffff;
    --photo-warm-a: #c8460f;
    --photo-warm-b: #7a2a0e;
    --photo-cool-a: #8fa9bd;
    --photo-cool-b: #4f6f8c;
    --photo-soft-a: #c9d8b6;
    --photo-soft-b: #eef0ea;
    --photo-family-a: #d9d4cc;
    --photo-family-b: #8d8275;
  }
  * { box-sizing: border-box; margin: 0; padding: 0; }
  html, body { width: 1200px; height: 2994px; overflow: hidden; background: var(--white); }
  body { font-family: "Roboto", sans-serif; color: var(--ink); position: relative; }
  .backdrop { position: absolute; inset: 0; width: 1200px; height: 2994px; }
  .abs { position: absolute; }

  .brand { left: 87px; top: 38px; font-size: 44px; font-weight: 700; color: var(--brand-green); letter-spacing: -1px; display: flex; align-items: center; gap: 10px; }
  .brand-dot { width: 16px; height: 16px; border-radius: 50%; background: var(--orange); }
  .menu-toggle { left: 1084px; top: 60px; width: 28px; }
  .menu-toggle span { display: block; height: 2px; background: var(--ink); margin-bottom: 5px; }

  .hero-kicker { left: 86px; top: 344px; font-size: 47px; font-weight: 400; line-height: 1; }
  .hero-title { left: 84px; top: 392px; font-size: 70px; font-weight: 700; line-height: 1; letter-spacing: -1px; }
  .hero-lead { left: 87px; top: 468px; width: 460px; font-size: 17px; line-height: 27px; font-weight: 500; }

  .service-title { font-size: 23px; font-weight: 500; color: var(--orange); }
  .service-text { font-size: 16.5px; line-height: 27px; width: 330px; }
  .svc-1-title { left: 220px; top: 918px; }
  .svc-1-text { left: 224px; top: 954px; }
  .svc-2-title { left: 692px; top: 919px; }
  .svc-2-text { left: 696px; top: 955px; }

  .section-title { font-size: 46px; font-weight: 400; line-height: 44px; }
  .section-text { font-size: 17.5px; line-height: 27px; font-weight: 500; }
  .care-title { left: 584px; top: 1352px; }
  .care-text { left: 585px; top: 1450px; width: 520px; }
  .care-text p { margin-bottom: 8px; }
  .about-title { left: 92px; top: 2068px; }
  .about-text { left: 93px; top: 2162px; width: 530px; }

  .btn { height: 40px; width: 153px; border-radius: 20px; font-size: 16px; font-weight: 500; display: flex; align-items: center; justify-content: center; text-transform: uppercase; }
  .btn-light { left: 585px; top: 1640px; background: var(--white); color: var(--ink); }
  .btn-orange { left: 93px; top: 2398px; background: var(--orange); color: var(--white); }

  .footer-brand { left: 250px; top: 2612px; font-size: 66px; font-weight: 700; color: var(--white); letter-spacing: -1px; display: flex; align-items: center; gap: 14px; }
  .footer-brand .brand-dot { width: 22px; height: 22px; background: var(--white); }
  .contact { top: 2780px; width: 260px; text-align: center; color: var(--white); }
  .contact svg { display: block; margin: 0 auto 8px; }
  .contact-label { font-size: 20px; font-weight: 700; line-height: 24px; }
  .contact-value { font-size: 17px; font-weight: 500; line-height: 22px; }
  .c-phone { left: 88px; }
  .c-fax { left: 310px; }
  .c-email { left: 576px; }
  .c-web { left: 841px; }
  .footer-rule { left: 0; top: 2938px; width: 1200px; height: 1px; background: rgba(255,255,255,0.25); }
  .to-top { left: 1135px; top: 2921px; width: 33px; height: 33px; border-radius: 50%; background: var(--lime); display: flex; align-items: center; justify-content: center; }
  .copyright { left: 0; top: 2958px; width: 1200px; text-align: center; font-size: 14px; color: var(--white); }
</style>
</head>
<body>

<svg class="backdrop" viewBox="0 0 1200 2994" xmlns="http://www.w3.org/2000/svg">
  <defs>
    <linearGradient id="warmPhoto" x1="0" y1="0" x2="1" y2="1">
      <stop offset="0" stop-color="var(--photo-warm-a)"/>
      <stop offset="1" stop-color="var(--photo-warm-b)"/>
    </linearGradient>
    <linearGradient id="coolPhoto" x1="0" y1="0" x2="1" y2="1">
      <stop offset="0" stop-color="var(--photo-cool-a)"/>
      <stop offset="1" stop-color="var(--photo-cool-b)"/>
    </linearGradient>
    <linearGradient id="softPhoto" x1="0" y1="0" x2="1" y2="1">
      <stop offset="0" stop-color="var(--photo-soft-a)"/>
      <stop offset="1" stop-color="var(--photo-soft-b)"/>
    </linearGradient>
    <linearGradient id="familyPhoto" x1="0" y1="0" x2="1" y2="1">
      <stop offset="0" stop-color="var(--photo-family-a)"/>
      <stop offset="1" stop-color="var(--photo-family-b)"/>
    </linearGradient>
  </defs>

  <!-- hero -->
  <path d="M790 46 C640 110 560 260 588 400 C618 560 720 670 812 712 C920 750 1100 750 1200 842 L1200 30 Z" fill="var(--lime)"/>
  <g role="img" aria-label="Photo of a smiling younger woman hugging an older woman at home">
    <path d="M820 78 C680 150 612 280 625 405 C642 545 745 650 840 686 C960 720 1100 730 1200 800 L1200 40 Z" fill="url(#warmPhoto)"/>
  </g>
  <circle cx="1150" cy="-180" r="450" fill="var(--sky)"/>

  <!-- lime band -->
  <path d="M0 848 C200 1120 420 1225 600 1225 C800 1225 1000 1180 1200 1120 L1200 1800 C1000 1782 800 1784 620 1790 C400 1800 150 1860 0 1894 Z" fill="var(--lime)"/>

  <!-- service circles -->
  <circle cx="383" cy="775" r="124" fill="var(--orange)"/>
  <circle cx="394" cy="768" r="112" fill="var(--lime)"/>
  <g role="img" aria-label="Photo of hands resting on a wheelchair handle">
    <circle cx="400" cy="762" r="106" fill="url(#coolPhoto)"/>
  </g>
  <circle cx="848" cy="763" r="134" fill="var(--lime)"/>
  <circle cx="866" cy="750" r="124" fill="var(--orange)"/>
  <g role="img" aria-label="Photo of a caregiver helping an older woman">
    <circle cx="872" cy="742" r="106" fill="url(#coolPhoto)"/>
  </g>

  <!-- caregivers circle -->
  <circle cx="310" cy="1500" r="217" fill="var(--orange)"/>
  <circle cx="337" cy="1484" r="204" fill="var(--lime)"/>
  <g role="img" aria-label="Photo of a caregiver with an older woman in a wheelchair outdoors">
    <circle cx="331" cy="1474" r="188" fill="url(#softPhoto)"/>
  </g>

  <!-- footer -->
  <path d="M0 2707 C150 2620 250 2470 380 2466 C520 2462 600 2600 750 2670 C900 2730 1100 2725 1200 2712 L1200 2994 L0 2994 Z" fill="var(--orange)"/>

  <!-- family blob -->
  <path d="M980 1938 C1080 1990 1160 2060 1200 2126 L1200 2650 C1100 2660 1000 2652 920 2640 Z" fill="var(--orange)"/>
  <path d="M690 1832 C640 1850 660 1960 720 2060 C800 2200 880 2320 820 2380 C740 2420 620 2420 612 2480 C620 2580 800 2640 950 2640 C1060 2640 1150 2620 1200 2600 L1200 2120 C1100 1960 900 1830 690 1832 Z" fill="var(--lime)"/>
  <g role="img" aria-label="Photo of a smiling family of four sitting together">
    <path d="M725 1850 C690 1880 710 1970 755 2060 C830 2210 905 2330 845 2400 C770 2445 650 2440 640 2490 C650 2570 810 2620 950 2622 C1060 2622 1150 2600 1200 2580 L1200 2140 C1100 1990 900 1860 725 1850 Z" fill="url(#familyPhoto)"/>
  </g>
</svg>

<header>
  <div class="abs brand">Brightpath<span class="brand-dot"></span></div>
  <div class="abs menu-toggle" aria-label="Menu"><span></span><span></span><span></span></div>
</header>

<section class="hero">
  <p class="abs hero-kicker">Live independently</p>
  <h1 class="abs hero-title">in your home!</h1>
  <p class="abs hero-lead">We Provide in-home care for people of all ages Call to receive FREE in-home assessment</p>
</section>

<section class="services">
  <h3 class="abs service-title svc-1-title">Companion and Personal Care</h3>
  <p class="abs service-text svc-1-text">24-Hours Live-in,Overnight,Full Time, Part Time, Respite Care and More We tailor each plan of care to the needs of the client</p>
  <h3 class="abs service-title svc-2-title">Exceptional One on One Care</h3>
  <p class="abs service-text svc-2-text">Our Kind natured and patient caregivers provide assistance to those who have diffi-culty with caring for themselves</p>
</section>

<section class="caregivers">
  <h2 class="abs section-title care-title">In-home private duty<br>caregivers</h2>
  <div class="abs section-text care-text">
    <p>At the Brightpath Home Partners, LLC we believe that a small group of caring and dedicated people create a dynamic culture that transforms lives.</p>
    <p>We provide in-home care for people of all ages. Our kind natured and patient caregivers provide assistance to those who have difficulty with caring for themselves.</p>
  </div>
  <a class="abs btn btn-light">Read More</a>
</section>

<section class="about">
  <h2 class="abs section-title about-title">Brightpath Home<br>Partners LLC</h2>
  <p class="abs section-text about-text">Work is a great part of one’s life. If you feel like life is passing you by and you feel stuck in mediocracy, then we invite you to do something new, something bold and to do it now. We invite you to alter your career path, increase your contentment at work, and transform the story of your life. Brightpath Home Partners, LLC offers career opportunities that are personally rewarding. You will feel personal satisfaction by providing care, assistance, and help to those most in need.</p>
  <a class="abs btn btn-orange">Read More</a>
</section>

<footer>
  <div class="abs footer-brand">Brightpath<span class="brand-dot"></span></div>

  <div class="abs contact c-phone">
    <svg width="32" height="32" viewBox="0 0 24 24"><path d="M6.6 10.8a15.1 15.1 0 0 0 6.6 6.6l2.2-2.2c.3-.3.7-.4 1-.2 1.1.4 2.3.6 3.6.6.6 0 1 .4 1 1V20c0 .6-.4 1-1 1C10.6 21 3 13.4 3 4c0-.6.4-1 1-1h3.5c.6 0 1 .4 1 1 0 1.3.2 2.5.6 3.6.1.3 0 .7-.2 1z" fill="var(--lime)"/></svg>
    <div class="contact-label">Phone</div>
    <div class="contact-value">555-014-2280</div>
  </div>
  <div class="abs contact c-fax">
    <svg width="38" height="34" viewBox="0 0 24 22"><rect x="6" y="1" width="12" height="5" fill="var(--lime)"/><rect x="1" y="7" width="22" height="9" rx="2" fill="var(--lime)"/><rect x="6" y="13" width="12" height="8" fill="var(--lime)" stroke="var(--orange)" stroke-width="1.2"/></svg>
    <div class="contact-label">Fax</div>
    <div class="contact-value">555-014-2291</div>
  </div>
  <div class="abs contact c-email">
    <svg width="38" height="32" viewBox="0 0 24 18"><rect x="0" y="0" width="24" height="18" rx="1.5" fill="var(--lime)"/><path d="M1 1.5 L12 10 L23 1.5" fill="none" stroke="var(--orange)" stroke-width="1.6"/></svg>
    <div class="contact-label">Email</div>
    <div class="contact-value">hello@brightpathhome.example</div>
  </div>
  <div class="abs contact c-web">
    <svg width="34" height="34" viewBox="0 0 24 24" fill="none" stroke="var(--lime)" stroke-width="1.6"><circle cx="12" cy="12" r="10"/><ellipse cx="12" cy="12" rx="4.5" ry="10"/><path d="M2 12h20M4 7h16M4 17h16"/></svg>
    <div class="contact-label">Web</div>
    <div class="contact-value">brightpathhome.example</div>
  </div>

  <div class="abs footer-rule"></div>
  <a class="abs to-top" aria-label="Back to top"><svg width="12" height="8" viewBox="0 0 12 8"><path d="M1 7 L6 2 L11 7" fill="none" stroke="var(--orange)" stroke-width="2"/></svg></a>
  <p class="abs copyright">Copyright 2019 | All Right Reserved</p>
</footer>

</body>
</html>
```